Home page for local retail aggregator

About us: We are a new company that showcases beautiful products available at nearby retail stores. This homepage is meant to display the latest products featured on our site and also allow the user to search, browse with filters, and access their account details.

Currently, our home page looks a little bland. We want the focus of the site to remain on the featured photos and products but the design should be more cohesive. The most successful designs will make more subtle use of our colors, provide intuitive menu controls, and look visually stunning.

This homepage has a few sections:

Header:
-Top Section: will always remain at the top of the page. There should be space for our company name ”zLantern”, a tagline, and a place for the menus.
-Menus: user must be able to find links for: “My profile” “My Products” “Add Product” “Preview store”
-Bottom section: this will scroll with the user and always remain at the top of the screen providing access to a search box, and filters for “location” “price” and retail categories.

Main Page:
-Each product featured is shown on a tile that includes a photo, title, price, name of store, has space to leave a comment, and include counters for "likes," comments, and "Pods"). “Pods” are bookmark folders. The user’s profile pic is also shown in miniature if they leave a comment.

The final version of the site must be delivered in a fully layered photoshop file and have versions demonstrating what the page will look like both when a user is logged-in and when logged-out.

Target Market(s)

Most of our users are female 18-45. Our customers are retail store owners who want their products to look attractive and professional.

Industry/Entity Type

Retail

Requirements
Must have
• Our logo must be present on the site (attached to project). You're welcome to change the colors in the header but it should look good with our logo.

For reference here are colors we're currently using:
Site text is in Dark Blue: RGB(10/23/47)
Logo color on business cards is light blue: (51/153/204)
Nice to have
• Would love to see new versions of the menus that are more modern and intuitive. Currently we just have links to each individual control. Putting these in a drop-down or re-arranging them would be nice.

```html
<!DOCTYPE html>
<html lang="en">
<head>
<meta charset="utf-8">
<title>zLantern — Local product search and discovery</title>
<link href="https://fonts.googleapis.com/css2?family=Cabin:wght@400;500;600&family=Arimo:wght@400;700&display=swap" rel="stylesheet">
<style>
:root{
  --header-top:#2d66b1;
  --header-bottom:#1d4e96;
  --page-bg:#e6e6e6;
  --ink:#0a172f;
  --brand:#1e4e93;
  --link:#1f4f97;
  --muted:#8a8a8a;
  --price:#e3447f;
  --tile:#ffffff;
  --strip:#ececec;
  --comment:#f2f2f2;
  --field:#efefef;
  --field-line:#d6d6d6;
  --icon:#5b4a5e;
}
*{box-sizing:border-box;margin:0;padding:0}
html,body{width:1200px;height:900px;overflow:hidden}
body{background:var(--page-bg);font-family:"Arimo",Arial,sans-serif;color:var(--ink);position:relative}

.site-header{position:absolute;left:0;top:0;width:1200px;height:66px;background:linear-gradient(var(--header-top),var(--header-bottom));box-shadow:0 1px 3px rgba(0,0,0,.3)}
.main-nav a{position:absolute;top:22px;font-family:"Cabin",sans-serif;font-size:15px;color:#fff;text-decoration:none}
.social{position:absolute;right:22px;top:21px;display:flex;gap:14px}
.social span{width:22px;height:22px;border-radius:50%;background:#fff}

.brand-badge{position:absolute;left:545px;top:6px;width:110px;height:110px;border-radius:50%;background:#f4f4f4;border:3px solid #d9dde3;box-shadow:0 2px 4px rgba(0,0,0,.15)}
.brand-name{position:absolute;left:0;width:1200px;top:110px;text-align:center;font-family:"Cabin",sans-serif;font-weight:600;font-size:22px;color:var(--brand)}
.tagline{position:absolute;left:0;width:1200px;top:140px;text-align:center;font-family:"Cabin",sans-serif;font-size:14px;color:#6a6a6a}

.filters{position:absolute;top:82px;left:19px;display:flex;gap:22px;font-family:"Cabin",sans-serif;font-size:15px;color:var(--brand)}
.filters span{display:flex;align-items:center;gap:7px}
.search{position:absolute;left:957px;top:79px;width:228px;height:25px;background:#fff;border:1px solid #d4d4d4;border-radius:2px;font-family:"Cabin",sans-serif;font-style:italic;font-size:11px;color:#444;padding:6px 9px}
.search-btn{position:absolute;right:0;top:0;width:24px;height:23px;background:#f1f1f1;border-left:1px solid #d4d4d4;display:flex;align-items:center;justify-content:center}

.wall{position:absolute;top:180px;left:7px;display:flex;gap:12px}
.column{width:188px;display:flex;flex-direction:column;gap:12px}
.tile{background:var(--tile);box-shadow:0 1px 2px rgba(0,0,0,.18);padding:8px 8px 0}
.tile-photo{width:100%}
.tile-info{position:relative;padding:7px 0 8px}
.tile-title{font-size:9px;color:var(--link);line-height:13px}
.tile-store{font-size:9px;color:var(--muted);line-height:13px}
.tile-price{position:absolute;right:0;top:16px;font-size:10px;font-weight:700;color:var(--price)}
.tile-stats{margin:0 -8px;height:20px;background:var(--strip);display:flex;align-items:center;gap:9px;padding:0 8px;font-size:9px;color:#777}
.tile-stats span{display:flex;align-items:center;gap:2px}
.comment{margin:0 -8px;background:var(--comment);border-top:1px solid #fff;display:flex;gap:6px;padding:9px 8px 8px;font-size:8.5px;line-height:12px;color:#333;min-height:44px}
.comment b{font-weight:700;color:#444}
.avatar{flex:none;width:24px;height:24px;border-radius:2px}
.more{margin:0 -8px;background:var(--comment);border-top:1px solid #fff;text-align:center;font-size:9px;font-weight:700;color:#333;padding:8px 0}
.comment-form{margin:0 -8px;display:flex;gap:8px;padding:8px 8px 8px}
.user-mark{flex:none;width:24px;height:24px;border-radius:2px;background:#2b2b2b}
.comment-field{flex:1;height:47px;background:var(--field);border:1px solid var(--field-line);font-size:9px;color:#666;padding:6px}
</style>
</head>
<body>
<svg width="0" height="0" style="position:absolute">
  <symbol id="i-like" viewBox="0 0 10 10"><rect x="0" y="4" width="2.5" height="6" fill="currentColor"/><path d="M3.5 4 6 0.5 7 1 6.5 4 10 4 9 10 3.5 10Z" fill="none" stroke="currentColor" stroke-width="1"/></symbol>
  <symbol id="i-comment" viewBox="0 0 14 10"><ellipse cx="6" cy="4.5" rx="5.5" ry="4" fill="currentColor"/><path d="M3 8 2 10 6 8Z" fill="currentColor"/></symbol>
  <symbol id="i-pod" viewBox="0 0 10 10"><rect x="1" y="0.5" width="8" height="9" fill="none" stroke="currentColor"/><rect x="3" y="2.5" width="4" height="5" fill="currentColor"/></symbol>
</svg>

<header class="site-header">
  <nav class="main-nav">
    <a href="#" style="left:329px">My Profile</a>
    <a href="#" style="left:426px">My Products</a>
    <a href="#" style="left:688px">Add Product</a>
    <a href="#" style="left:795px">Preview store</a>
  </nav>
  <div class="social"><span role="img" aria-label="Social link"></span><span role="img" aria-label="Social link"></span><span role="img" aria-label="Social link"></span></div>
</header>

<div class="brand-badge" role="img" aria-label="zLantern badge"></div>
<div class="brand-name">zLantern</div>
<div class="tagline">Local product search and discovery</div>

<div class="filters">
  <span><svg width="16" height="22" viewBox="0 0 16 22"><path d="M8 0C3.6 0 0 3.4 0 7.8 0 13 8 22 8 22s8-9 8-14.2C16 3.4 12.4 0 8 0Z" fill="var(--icon)"/><circle cx="8" cy="7.5" r="2.8" fill="#fff"/></svg>Location</span>
  <span><svg width="20" height="20" viewBox="0 0 20 20"><path d="M9 1h9v9l-8 9-9-9Z" fill="var(--icon)" transform="rotate(-20 10 10)"/><circle cx="14" cy="5" r="1.6" fill="#fff"/></svg>Price</span>
  <span><svg width="24" height="20" viewBox="0 0 24 20"><path d="M1 7 4 1h16l3 6Z" fill="var(--icon)"/><rect x="3" y="8" width="18" height="11" fill="var(--icon)"/><rect x="6" y="11" width="5" height="8" fill="#fff"/></svg>Retail Categories</span>
</div>
<div class="search">What do you want to discover today?
  <span class="search-btn"><svg width="11" height="11" viewBox="0 0 11 11"><circle cx="4.5" cy="4.5" r="3.3" fill="none" stroke="#555" stroke-width="1.5"/><path d="M7 7l3 3" stroke="#555" stroke-width="1.8"/></svg></span>
</div>

<main class="wall">
  <section class="column">
    <article class="tile">
      <div class="tile-photo" role="img" aria-label="White and navy colorblock dress on a hanger" style="height:209px;background:linear-gradient(#efede9 0%,#f3f1ee 40%,#2a3a5e 62%,#243352 100%)"></div>
      <div class="tile-info"><div class="tile-title">Navy Lucette Colorblock Dress</div><div class="tile-store">Minimal</div><div class="tile-price">$50.00</div></div>
      <div class="tile-stats"><span>10<svg width="10" height="10"><use href="#i-like"/></svg></span><span>3<svg width="14" height="10"><use href="#i-comment"/></svg></span><span>50<svg width="10" height="10"><use href="#i-pod"/></svg></span></div>
      <div class="comment"><div class="avatar" role="img" aria-label="Member photo" style="background:#6f7d5a"></div><div><b>Kara Vance</b> onto <b>Favorite Things</b></div></div>
      <div class="comment"><div class="avatar" role="img" aria-label="Member photo" style="background:#7a5b4c"></div><div><b>Joel Ramsey</b> This is awesome!</div></div>
      <div class="comment"><div class="avatar" role="img" aria-label="Member photo" style="background:#4e3b33"></div><div><b>Rosa Abbott</b> Awesome</div></div>
      <div class="comment-form"><div class="user-mark" role="img" aria-label="Your profile picture"></div><div class="comment-field">Don't you love this?</div></div>
    </article>
    <article class="tile">
      <div class="tile-photo" role="img" aria-label="Cream ruffled one-shoulder dress with brown sash" style="height:208px;background:linear-gradient(#e2ddd4,#efe9df 50%,#d9d2c6)"></div>
    </article>
  </section>

  <section class="column">
    <article class="tile">
      <div class="tile-photo" role="img" aria-label="Legs in kitten-print tights with pink shoes" style="height:256px;background:linear-gradient(#dcb3a4,#d8a89c 60%,#e9b8c4)"></div>
      <div class="tile-info"><div class="tile-title">Kitten Stockings! Soo cute! I love it</div><div class="tile-store">Minimal</div><div class="tile-price">$10.00</div></div>
      <div class="tile-stats"><span>90<svg width="10" height="10"><use href="#i-like"/></svg></span><span>1<svg width="14" height="10"><use href="#i-comment"/></svg></span><span>20<svg width="10" height="10"><use href="#i-pod"/></svg></span></div>
      <div class="comment"><div class="avatar" role="img" aria-label="Member photo" style="background:#8a6a55"></div><div><b>Tessa McKinley Orr</b> via <b>Anna Weller</b> onto <b>Craft Ideas</b></div></div>
      <div class="comment-form"><div class="user-mark" role="img" aria-label="Your profile picture"></div><div class="comment-field">This is wonderful?</div></div>
    </article>
    <article class="tile">
      <div class="tile-photo" role="img" aria-label="Person wearing blue jeans, seen from behind" style="height:208px;background:linear-gradient(#cfcac2,#5e7ca2 25%,#4c6a92 75%,#a99a86)"></div>
      <div class="tile-info"><div class="tile-title">Blue Jeans</div><div class="tile-store">Jean and Jeans Co.</div><div class="tile-price">$60.00</div></div>
    </article>
  </section>

  <section class="column">
    <article class="tile">
      <div class="tile-photo" role="img" aria-label="Four lipstick colours: black, pink, orange and blue" style="height:108px;background:linear-gradient(90deg,#3a2b33 0%,#d44fd0 50%,#f08a3a 50%,#4fc2e2 100%)"></div>
      <div class="tile-info"><div class="tile-title">Lip for a lip</div><div class="tile-store">Kiss</div><div class="tile-price">$30.00</div></div>
      <div class="tile-stats"><span>90<svg width="10" height="10"><use href="#i-like"/></svg></span><span>1<svg width="14" height="10"><use href="#i-comment"/></svg></span><span>45<svg width="10" height="10"><use href="#i-pod"/></svg></span></div>
      <div class="comment"><div class="avatar" role="img" aria-label="Member photo" style="background:#7d6c4f"></div><div><b>Reese Porter</b> via <b>Amy Blake</b> onto <b>Lovely Tresses</b></div></div>
      <div class="comment-form"><div class="user-mark" role="img" aria-label="Your profile picture"></div><div class="comment-field">Don't you love this?</div></div>
    </article>
    <article class="tile">
      <div class="tile-photo" role="img" aria-label="Outfit set: trench coat, white shirt, jeans, bag and flats" style="height:218px;background:linear-gradient(90deg,#ead6c8 0%,#f6f2ee 55%,#3d5577 90%)"></div>
      <div class="tile-info"><div class="tile-title">My Collection</div><div class="tile-store">Collect them all</div><div class="tile-price">$130.00</div></div>
      <div class="tile-stats"><span>90<svg width="10" height="10"><use href="#i-like"/></svg></span><span>6<svg width="14" height="10"><use href="#i-comment"/></svg></span><span>45<svg width="10" height="10"><use href="#i-pod"/></svg></span></div>
      <div class="comment"><div class="avatar" role="img" aria-label="Member photo" style="background:#3f5f86"></div><div><b>Alan n Dana Brooks</b> Pushed play today for the first time in months. I have to say it felt great!!!!</div></div>
      <div class="comment"><div class="avatar" role="img" aria-label="Member photo" style="background:#6b6b6b"></div><div><b>Tina DeLuca</b> @Elle Parker</div></div>
    </article>
  </section>

  <section class="column">
    <article class="tile">
      <div class="tile-photo" role="img" aria-label="Outfit set: trench coat, white shirt, jeans, bag and flats" style="height:218px;background:linear-gradient(90deg,#ead6c8 0%,#f6f2ee 55%,#3d5577 90%)"></div>
      <div class="tile-info"><div class="tile-title">My Collection</div><div class="tile-store">Collect them all</div><div class="tile-price">$130.00</div></div>
      <div class="tile-stats"><span>90<svg width="10" height="10"><use href="#i-like"/></svg></span><span>6<svg width="14" height="10"><use href="#i-comment"/></svg></span><span>45<svg width="10" height="10"><use href="#i-pod"/></svg></span></div>
      <div class="comment"><div class="avatar" role="img" aria-label="Member photo" style="background:#3f5f86"></div><div><b>Alan n Dana Brooks</b> Pushed play today for the first time in months. I have to say it felt great!!!!</div></div>
      <div class="comment"><div class="avatar" role="img" aria-label="Member photo" style="background:#6b6b6b"></div><div><b>Tina DeLuca</b> @Elle Parker</div></div>
      <div class="comment"><div class="avatar" style="background:#d0202f"></div><div><b>Jodie Jensen</b> I have a love-hate relationship with this man!</div></div>
      <div class="comment"><div class="avatar" role="img" aria-label="Member photo" style="background:#5a6f86"></div><div><b>Kira Mason</b> I'm thinking of starting FitBlast 2 soon. I'm so excited!</div></div>
      <div class="comment"><div class="avatar" role="img" aria-label="Member photo" style="background:#8c4f4a"></div><div><b>Alina Mae</b> I'm in love with him. SO fun to watch during my workouts.</div></div>
      <div class="more">All 6 comments...</div>
      <div class="comment-form"><div class="user-mark" role="img" aria-label="Your profile picture"></div><div class="comment-field">This is wonderful?</div></div>
    </article>
    <article class="tile">
      <div class="tile-photo" role="img" aria-label="Four lipstick colours" style="height:40px;background:linear-gradient(90deg,#3a2b33 0%,#d44fd0 100%)"></div>
    </article>
  </section>

  <section class="column">
    <article class="tile">
      <div class="tile-photo" role="img" aria-label="Person wearing blue jeans, seen from behind" style="height:209px;background:linear-gradient(#cfcac2,#5e7ca2 25%,#4c6a92 75%,#a99a86)"></div>
      <div class="tile-info"><div class="tile-title">Blue Jeans</div><div class="tile-store">Jean and Jeans Co.</div><div class="tile-price">$60.00</div></div>
      <div class="tile-stats"><span>10<svg width="10" height="10"><use href="#i-like"/></svg></span><span>3<svg width="14" height="10"><use href="#i-comment"/></svg></span><span>50<svg width="10" height="10"><use href="#i-pod"/></svg></span></div>
      <div class="comment"><div class="avatar" role="img" aria-label="Member photo" style="background:#6f7d5a"></div><div><b>Kara Vance</b> onto <b>Favorite Things</b></div></div>
      <div class="comment"><div class="avatar" role="img" aria-label="Member photo" style="background:#7a5b4c"></div><div><b>Joel Ramsey</b> This is awesome!</div></div>
      <div class="comment"><div class="avatar" role="img" aria-label="Member photo" style="background:#4e3b33"></div><div><b>Rosa Abbott</b> Awesome</div></div>
      <div class="comment-form"><div class="user-mark" role="img" aria-label="Your profile picture"></div><div class="comment-field">Don't you love this?</div></div>
    </article>
    <article class="tile">
      <div class="tile-photo" role="img" aria-label="Legs in kitten-print tights with pink tulle" style="height:220px;background:linear-gradient(#e6b9b6,#dcb0a2 60%,#d9a99d)"></div>
    </article>
  </section>

  <section class="column">
    <article class="tile">
      <div class="tile-photo" role="img" aria-label="Cream ruffled one-shoulder dress with brown sash" style="height:209px;background:linear-gradient(#e2ddd4,#efe9df 50%,#d9d2c6)"></div>
      <div class="tile-info"><div class="tile-title">Dress like</div><div class="tile-store">You and Me Co.</div><div class="tile-price">$60.00</div></div>
      <div class="tile-stats"><span>10<svg width="10" height="10"><use href="#i-like"/></svg></span><span>2<svg width="14" height="10"><use href="#i-comment"/></svg></span><span>50<svg width="10" height="10"><use href="#i-pod"/></svg></span></div>
      <div class="comment"><div class="avatar" role="img" aria-label="Member photo" style="background:#9a7b5c"></div><div><b>Laila Stone</b> onto <b>Quotes</b></div></div>
      <div class="comment"><div class="avatar" role="img" aria-label="Member photo" style="background:#8a5a4e"></div><div><b>Kelsey Wade-Hollis</b> love, love, love</div></div>
      <div class="comment-form"><div class="user-mark" role="img" aria-label="Your profile picture"></div><div class="comment-field">Don't you love this?</div></div>
    </article>
    <article class="tile">
      <div class="tile-photo" role="img" aria-label="White and navy colorblock dress on a hanger" style="height:210px;background:linear-gradient(#efede9 0%,#f3f1ee 40%,#2a3a5e 62%,#243352 100%)"></div>
      <div class="tile-info"><div class="tile-title">Navy Lucette Colorblock Dress</div><div class="tile-store">Minimal</div><div class="tile-price">$50.00</div></div>
    </article>
  </section>
</main>
</body>
</html>
```